Book Cover for Political Biography

Back round color, darker green.

This book is a political biography of Mr. Van Oosterwijk who was a prominent politician in Curacao.

Looking for a modern toward the conservative look. The attached images can be used as place holders, we will get hi resolution ones to replace.

Book Title:
Mr. Dr. Hendrik van Oosterwijk: Pleitbezorger van de Bestuurlijke Vernieuwing der Caribische Eilanden

Name Author:
drs. T.J. (Willem) Harkstede MBA

Please leave space on the back for book description (one paragraph) and author biography (short paragraph)

```html
<!DOCTYPE html>
<html lang="nl">
<head>
<meta charset="utf-8">
<title>Van Oosterwijk – Book Cover</title>
<link rel="stylesheet" href="https://fonts.googleapis.com/css2?family=Gelasio:wght@400;500&display=swap">
<style>
  :root {
    --green: #1c5a17;
    --green-deep: #164a12;
    --beige: #d9cfb2;
    --beige-light: #e8dfc4;
    --ink-light: #e6ddc3;
    --page: #ececec;
    --photo-dark: #6b6358;
    --photo-light: #cfc7b8;
  }
  * { margin: 0; padding: 0; box-sizing: border-box; }
  html, body { width: 1200px; height: 900px; overflow: hidden; background: var(--page); }
  body { position: relative; font-family: "Gelasio", Georgia, serif; }

  .cover {
    position: absolute; left: 82px; top: 72px; width: 1038px; height: 750px;
    background: var(--green);
  }
  .band { position: absolute; left: 0; width: 100%; }
  .band--top { top: 0; height: 375px; background: var(--green); }
  .band--middle {
    top: 381px; height: 276px; background: var(--beige);
    border-top: 2px solid var(--beige-light);
  }
  .band--middle::before, .band--middle::after {
    content: ""; position: absolute; left: 0; width: 100%; height: 3px; background: var(--green);
  }
  .band--middle::before { top: 2px; }
  .band--middle::after { bottom: 4px; }
  .band--bottom { top: 663px; height: 87px; background: var(--green); border-top: 2px solid var(--beige-light); }

  .spine-fold { position: absolute; top: 0; width: 1px; height: 100%; background: rgba(255,255,255,0.12); }
  .spine-fold--left { left: 500px; }
  .spine-fold--right { left: 538px; }

  .portrait {
    position: absolute; left: 16px; top: 33px; width: 144px; height: 208px;
    border: 2px solid var(--beige-light);
    background: linear-gradient(160deg, #d8d6d0 0%, #8f8c86 55%, #4a4844 100%);
  }
  .author-photo-slot {
    position: absolute; left: 16px; top: 414px; width: 144px; height: 208px;
    border: 2px solid var(--green); background: var(--beige);
  }
  .front-photo {
    position: absolute; left: 538px; top: 0; width: 500px; height: 375px;
    background: linear-gradient(100deg, var(--photo-dark) 0%, #9a9184 45%, var(--photo-light) 100%);
  }

  .blurb { position: absolute; left: 182px; width: 295px; font-size: 13.2px; line-height: 15.3px; text-align: justify; }
  .blurb h2 { font-size: 13.2px; font-weight: 400; text-align: left; }
  .blurb--description { top: 32px; color: var(--ink-light); }
  .blurb--biography { top: 412px; color: var(--green); }

  .spine-title {
    position: absolute; left: 519px; top: 52px; transform-origin: 0 0;
    transform: rotate(90deg) translateY(-50%);
    font-size: 31px; color: var(--ink-light); white-space: nowrap; letter-spacing: 0.5px;
  }
  .spine-author {
    position: absolute; left: 519px; top: 388px; transform-origin: 0 0;
    transform: rotate(90deg) translateY(-50%);
    font-size: 14.5px; color: var(--green); white-space: nowrap;
  }

  .front-title { position: absolute; left: 560px; width: 460px; text-align: center; color: var(--green); }
  .front-title__first { top: 424px; font-size: 34px; font-variant: small-caps; letter-spacing: 1px; line-height: 1; }
  .front-title__last { top: 476px; font-size: 44px; line-height: 1; }
  .front-rule { position: absolute; left: 563px; top: 537px; width: 448px; height: 2px; background: var(--green); }
  .front-subtitle {
    position: absolute; left: 546px; width: 488px; top: 555px; text-align: center;
    font-size: 19.5px; line-height: 29px; color: #1d2a18;
  }
  .front-author {
    position: absolute; left: 560px; width: 460px; top: 705px; text-align: center;
    font-size: 17px; color: var(--ink-light);
  }
</style>
</head>
<body>
  <div class="cover">
    <div class="band band--top"></div>
    <div class="band band--middle"></div>
    <div class="band band--bottom"></div>
    <div class="spine-fold spine-fold--left"></div>
    <div class="spine-fold spine-fold--right"></div>

    <div class="portrait" role="img" aria-label="Black-and-white portrait photograph of Mr. Dr. Hendrik van Oosterwijk"></div>
    <section class="blurb blurb--description">
      <h2>Book Description</h2>
      <p>Lorem ipsum dolor sit amet, consectetur diam adipiscing elit. Pellentesque mollis convallis lorem volutpat. Aliquam erat volutpat. Integer et vel aliquet elit, at mattis lorem. Integer et vel iaculis nulla tellus. Phasellus sed nulla dui. De Vivamus egestas ante at ultricies malesuada. Phasellus aliquam libero vel diam sagittis, a dignissim nunc commodo.</p>
    </section>

    <div class="author-photo-slot" role="img" aria-label="Placeholder for author photograph"></div>
    <section class="blurb blurb--biography">
      <h2>Author Biography</h2>
      <p>Lorem ipsum dolor sit amet, consectetur diam adipiscing elit. Pellentesque mollis convallis lorem volutpat. Aliquam erat volutpat. Integer et vel aliquet elit, at mattis lorem. Integer et vel iaculis nulla tellus. Phasellus sed nulla dui. De Vivamus egestas ante at ultricies malesuada. Phasellus aliquam libero vel diam sagittis, a dignissim nunc commodo.</p>
    </section>

    <div class="spine-title">VAN OOSTERWIJK</div>
    <div class="spine-author">drs. T.J. (Willem) Harkstede MBA</div>

    <div class="front-photo" role="img" aria-label="Sepia photograph of Van Oosterwijk speaking at a table beside a colleague in a white suit"></div>
    <h1>
      <span class="front-title front-title__first">Mr. Dr. Hendrik</span>
      <span class="front-title front-title__last">VAN OOSTERWIJK</span>
    </h1>
    <div class="front-rule"></div>
    <p class="front-subtitle">Pleitbezorger van de Bestuurlijke Vernieuwing<br>der Caribische Eilanden</p>
    <p class="front-author">drs. T.J. (Willem) Harkstede MBA</p>
  </div>
</body>
</html>
```